Book cover Design for her new book called 'Walking a path lined with courage and grace'

My name is Velorashi, I am the founder of The Quiet Lantern.
http://velorashi-wren.examplestore.com/
My book is an inspirational story of love and triumphing from adversity. After 40 years of surviving a life full of sexual abuse, physical and mental abuse and living with the effects of poor self-esteem and post traumatic stress disorder, this book is a guide to help others navigate away from negative emotions and help them find their own light in life. With the techniques developed and described in the book The Quiet Lantern's mission is to empower people with the journey to their own hearts and create warmth, love and inspiration.
The colours in the website represent the softness that I love and I prefer flowers. The colour also can be soft as well as vibrant and feminine. The final design should represent healing, love, inspiration and passion.

Target Market(s)

Women over the age of 25 -80
Teenagers suffering from depression
Men and women suffering from poor self esteem
Woman who have poor self confidence.

Requirements
Should not have
• Should not be dark in colour or imagery.

```html
<!DOCTYPE html>
<html lang="en">
<head>
<meta charset="utf-8">
<title>Walking a path lined with courage and grace — Velorashi</title>
<link href="https://fonts.googleapis.com/css2?family=Oswald:wght@300;500&family=Caveat:wght@400&display=swap" rel="stylesheet">
<style>
  :root {
    --paper: #ffffff;
    --title-purple: #8d4c9f;
    --ink: #1b1b1f;
    --photo-light: #c9dbe6;
    --photo-mid: #7f9cb3;
    --photo-dark: #3b2f3c;
    --blossom: #f4f2ee;
    --leaf: #9fb86a;
  }
  * { margin: 0; padding: 0; box-sizing: border-box; }
  html, body {
    width: 769px;
    height: 1200px;
    overflow: hidden;
    background: var(--paper);
  }
  .cover {
    position: relative;
    width: 769px;
    height: 1200px;
    background: var(--paper);
  }
  .title {
    position: absolute;
    top: 86px;
    left: 0;
    width: 769px;
    text-align: center;
    font-family: "Oswald", sans-serif;
    font-weight: 500;
    font-size: 90px;
    line-height: 1;
    letter-spacing: 9px;
    color: var(--title-purple);
    text-transform: uppercase;
  }
  .subtitle {
    position: absolute;
    top: 172px;
    right: 96px;
    font-family: "Caveat", cursive;
    font-size: 46px;
    line-height: 1;
    color: var(--ink);
  }
  .cover-photo {
    position: absolute;
    left: 124px;
    top: 404px;
    width: 522px;
    height: 522px;
  }
  .tagline {
    position: absolute;
    top: 1036px;
    left: 0;
    width: 769px;
    text-align: center;
    font-family: "Caveat", cursive;
    font-size: 17px;
    letter-spacing: 0.5px;
    color: var(--ink);
  }
  .author {
    position: absolute;
    top: 1052px;
    left: 0;
    width: 769px;
    text-align: center;
    font-family: "Oswald", sans-serif;
    font-weight: 300;
    font-size: 72px;
    line-height: 1;
    letter-spacing: 7px;
    color: var(--ink);
    text-transform: uppercase;
  }
</style>
</head>
<body>
  <main class="cover">
    <h1 class="title">Walking a path</h1>
    <p class="subtitle">lined with courage and grace</p>

    <svg class="cover-photo" viewBox="0 0 522 522" role="img" aria-label="Photograph of white blossoms with fresh green leaves on a branch against a soft blue sky">
      <defs>
        <radialGradient id="photoTone" cx="0.4" cy="0.55" r="0.7">
          <stop offset="0" stop-color="var(--blossom)"/>
          <stop offset="0.25" stop-color="var(--photo-light)"/>
          <stop offset="0.6" stop-color="var(--photo-mid)"/>
          <stop offset="1" stop-color="var(--photo-dark)"/>
        </radialGradient>
      </defs>
      <circle cx="261" cy="261" r="259" fill="url(#photoTone)"/>
    </svg>

    <p class="tagline">an inspiring book of overcoming adversity by</p>
    <p class="author">Velorashi</p>
  </main>
</body>
</html>
```